Harrow Collective
Chartered accountants & business advisors company seeks logo & business card design refresh - Financial Services
Simple
Derek Ostrander
Senior Project Accountant
PO Box 27 458 Wellington 6571
derek@harrowcollective.example.nz
harrowcollective.example.nz
Full Bleed Size (starting document size) 94 x 58 mm 1110 x 685 pixels * Finished artwork should use the full bleed dimensions for best results. Document Trim Size (final size after being cut) 91 x 55 mm 1075 x 650 pixels * Please be sure to keep all text within the safe margin. Resolution 300 DPI
Simple, perhaps solid colour with the web address (and logo etc)

```html
<!DOCTYPE html>
<html lang="en">
<head>
<meta charset="utf-8">
<title>Harrow Collective – Business Card</title>
<link href="https://fonts.googleapis.com/css2?family=Cinzel:wght@500&family=Crimson+Text:wght@400;600&display=swap" rel="stylesheet">
<style>
  :root {
    --blue: #2f86d0;
    --blue-light: #4fa3e4;
    --blue-deep: #1f6db5;
    --white: #ffffff;
    --ink: #3a4450;
    --ink-soft: #6b7683;
    --backdrop: #e9ecef;
  }
  html, body {
    margin: 0;
    padding: 0;
    width: 1200px;
    height: 908px;
    overflow: hidden;
    background: var(--backdrop);
  }
  .sheet {
    width: 1200px;
    height: 908px;
    display: flex;
    flex-direction: column;
    align-items: center;
    justify-content: center;
    gap: 36px;
  }
  .card {
    position: relative;
    width: 680px;
    height: 410px;
    border-radius: 26px;
    overflow: hidden;
    box-shadow: 0 6px 18px rgba(0,0,0,0.12);
  }
  .card-front {
    background: linear-gradient(135deg, var(--blue-light) 0%, var(--blue) 55%, var(--blue-deep) 100%);
    display: flex;
    align-items: center;
    justify-content: center;
  }
  .brand-name {
    font-family: "Cinzel", serif;
    font-weight: 500;
    letter-spacing: 4px;
    margin: 0;
    line-height: 1;
    white-space: nowrap;
  }
  .card-front .brand-name {
    color: var(--white);
    font-size: 40px;
  }
  .card-back {
    background: var(--white);
  }
  .edge-bands {
    position: absolute;
    inset: 0;
  }
  .back-brand {
    position: absolute;
    left: 70px;
    bottom: 62px;
  }
  .card-back .brand-name {
    color: var(--blue);
    font-size: 28px;
    letter-spacing: 3px;
  }
  .contact {
    position: absolute;
    left: 380px;
    top: 48px;
    font-family: "Crimson Text", serif;
    color: var(--ink);
  }
  .contact-name {
    margin: 0;
    font-size: 21px;
    font-weight: 600;
    color: var(--blue);
  }
  .contact-title {
    margin: 2px 0 18px;
    font-size: 15px;
    color: var(--ink-soft);
  }
  .contact-address {
    margin: 0 0 14px;
    font-size: 16px;
    line-height: 1.3;
    font-style: normal;
  }
  .contact-list {
    list-style: none;
    margin: 0;
    padding: 0;
    font-size: 15.5px;
    line-height: 1.55;
  }
  .contact-list li {
    display: flex;
    align-items: center;
    gap: 7px;
  }
  .contact-icon {
    width: 14px;
    height: 14px;
    flex: none;
  }
</style>
</head>
<body>
<main class="sheet">
  <section class="card card-front" aria-label="Card front">
    <p class="brand-name">Harrow Collective</p>
  </section>

  <section class="card card-back" aria-label="Card back">
    <svg class="edge-bands" viewBox="0 0 680 410" aria-hidden="true">
      <path d="M0 0 H34 Q14 205 34 410 H0 Z" fill="var(--blue)"/>
      <path d="M680 0 H646 Q666 205 646 410 H680 Z" fill="var(--blue)"/>
    </svg>

    <div class="contact">
      <p class="contact-name">Derek Ostrander</p>
      <p class="contact-title">Senior Project Accountant</p>
      <address class="contact-address">PO Box 27 458<br>Wellington 6571</address>
      <ul class="contact-list">
        <li>
          <svg class="contact-icon" viewBox="0 0 14 14" aria-hidden="true"><circle cx="7" cy="7" r="7" fill="var(--blue)"/><path d="M4.5 3.5l1.4 0 .6 1.8-.9.7a5 5 0 0 0 2.4 2.4l.7-.9 1.8.6v1.4c-3.5.3-6.3-2.5-6-6z" fill="var(--white)"/></svg>
          0800 555 017 (Toll Free)
        </li>
        <li>
          <svg class="contact-icon" viewBox="0 0 14 14" aria-hidden="true"><circle cx="7" cy="7" r="7" fill="var(--blue)"/><rect x="5" y="3" width="4" height="8" rx="0.8" fill="var(--white)"/></svg>
          +64 21 555 0142
        </li>
        <li>
          <svg class="contact-icon" viewBox="0 0 14 14" aria-hidden="true"><circle cx="7" cy="7" r="7" fill="var(--blue)"/><rect x="3.5" y="4.5" width="7" height="5" fill="var(--white)"/><path d="M3.5 4.5l3.5 3 3.5-3" fill="none" stroke="var(--blue)" stroke-width="0.8"/></svg>
          derek@harrowcollective.example.nz
        </li>
        <li>
          <svg class="contact-icon" viewBox="0 0 14 14" aria-hidden="true"><circle cx="7" cy="7" r="7" fill="var(--blue)"/><circle cx="7" cy="7" r="3.6" fill="none" stroke="var(--white)" stroke-width="0.9"/><path d="M3.4 7h7.2M7 3.4c-1.6 2-1.6 5.2 0 7.2M7 3.4c1.6 2 1.6 5.2 0 7.2" fill="none" stroke="var(--white)" stroke-width="0.7"/></svg>
          harrowcollective.example.nz
        </li>
      </ul>
    </div>

    <div class="back-brand">
      <p class="brand-name">Harrow Collective</p>
    </div>
  </section>
</main>
</body>
</html>
```